Startup Jewelry Needs a fully coded Ecommerce Website

Description

We want the full coded woocommerce website - website to be operational and fully integrated with Tendrix and other gateways .
We sell jewelry items like rings,ear rings,chain, necklaces etc.

Color Preference
Colors to be used are Velvet red, Black / anthracite, exclusive colors, silver-white, bronze-brown and golden.

Functionalities
Regarding Functions, the store will have functions of typical ecommerce jewelry store using the products/categories for the starting page, going into individual product pages by clicking these images and then leading to a detailed page for one product only.

Target Market
Jewelry-lovers, who appreciate extraordinary things, creative economy/fashion-industries, stylists, Style consultants, outfitter, theaters, operas, production sites, Cocktail-, Dinner and Bride-fashion etc

Look and Feel
Each slider illustrates characteristics of the customer's brand and the style your web design should communicate.

Must have
Logo must be designed

Should Not Have:
- - Dull and common design
- - Messy/unstructured navigation

Industry/Entity Type

Jewelry

Coding

Coded - Design and coding required

```html
<!DOCTYPE html>
<html lang="en">
<head>
<meta charset="utf-8">
<title>Jewelry – Online Store</title>
<link href="https://fonts.googleapis.com/css2?family=Oswald:wght@400;500&family=Arvo:wght@700&family=Open+Sans:wght@400;600&display=swap" rel="stylesheet">
<style>
:root{
  --bg:#d9dadc;
  --page:#1c1c1c;
  --page-dark:#070707;
  --footer:#050505;
  --footer-base:#0e0e0e;
  --bronze:#a47e5d;
  --bronze-light:#c9a584;
  --bronze-pale:#e7d3bf;
  --text:#ffffff;
  --muted:#8a8a8a;
  --line:#2a2a2a;
  --white:#ffffff;
  --card-line:#e4e4e4;
}
*{margin:0;padding:0;box-sizing:border-box}
html,body{width:1200px;height:1200px;overflow:hidden;background:var(--bg)}
body{font-family:"Open Sans",Arial,sans-serif;color:var(--text);position:relative}
.page{position:absolute;left:138px;top:26px;width:770px;height:956px;transform:scale(1.2);transform-origin:0 0;
  background:linear-gradient(180deg,#131313 0%,#262626 40%,#1a1a1a 75%,#202020 100%);overflow:hidden}
.abs{position:absolute}

.welcome{left:91px;top:11px;width:114px;height:17px;background:linear-gradient(#d9bea3,#a8866a);border-radius:2px;
  font:500 9.5px "Oswald",sans-serif;color:#2a1d12;text-align:center;line-height:17px}
.top-links{right:90px;top:18px;display:flex;gap:9px;font-size:6px;letter-spacing:.4px;color:#ddd}
.top-links span.sep{color:#777}
.cart{right:90px;top:42px;font-size:7px;color:#ddd;display:flex;align-items:center;gap:4px}
.logo{left:95px;top:52px;font:600 27px "Open Sans",sans-serif;color:#d6d6d6;letter-spacing:.3px}
.search{left:494px;top:70px;width:186px;height:28px;background:#0a0a0a;border-radius:4px;padding:5px;display:flex;gap:4px}
.search .field{flex:1;background:#fff;border-radius:2px;font-size:7px;color:#333;padding-left:6px;line-height:17px}
.search .btn{width:26px;background:linear-gradient(#d3b496,#9b7859);border-radius:2px;display:flex;align-items:center;justify-content:center}
.nav{left:91px;top:100px;width:589px;height:41px;display:flex;border:1px solid #333;border-radius:3px;background:#0d0d0d}
.nav a{flex:1;display:flex;align-items:center;justify-content:center;font:400 9.5px "Oswald",sans-serif;color:#fff;border-right:1px solid #2c2c2c;text-decoration:none}
.nav a:last-child{border-right:0}
.nav a.active{background:#242424}

.hero-glow{left:150px;top:140px;width:480px;height:230px;background:radial-gradient(ellipse at 40% 50%,rgba(90,90,90,.45),transparent 65%)}
.hero-img{left:185px;top:162px;width:140px;height:172px;border-radius:40% 40% 45% 45%;background:radial-gradient(circle at 45% 40%,#e7c08f,#a97a4a 55%,#5a3c22);opacity:.9}
.arrow{width:40px;height:40px;border-radius:50%;background:#0c0c0c;box-shadow:0 0 0 1px #333;display:flex;align-items:center;justify-content:center}
.hero-title{left:368px;top:198px;font:700 25px "Arvo",serif;color:#fff;letter-spacing:.5px}
.hero-sub{left:368px;top:240px;font:700 12px "Arvo",serif;color:#111;text-shadow:0 0 1px #555,0 1px 0 #444;letter-spacing:.3px}
.shop{left:368px;top:271px;width:146px;height:35px;border-radius:18px;background:linear-gradient(#d4b293,#9c7657);display:flex;align-items:center}
.shop .ico{width:54px;height:35px;border-radius:18px;background:#0b0b0b;display:flex;align-items:center;justify-content:center}
.shop span{font:700 11px "Arvo",serif;color:#fff;margin-left:8px}
.dots{left:370px;top:341px;display:flex;gap:8px}
.dots i{width:4px;height:4px;border-radius:50%;background:#555;display:block}
.dots i:first-child{background:var(--bronze-light)}

.promo{left:91px;top:354px;width:589px;height:118px;background:var(--white);border-radius:4px;padding:11px 9px;display:flex;gap:14px}
.promo .banner{flex:1;border-radius:3px;background:linear-gradient(90deg,#a98566,#e3ccb6 50%,#b39072);position:relative;color:#1a1a1a}
.promo .banner .pic{position:absolute;left:10px;top:8px;width:70px;height:78px;border-radius:6px;background:radial-gradient(circle,#d9d9d9,#8a6f58 70%);opacity:.8}
.b1 .t1{position:absolute;left:88px;top:22px;font:600 14px "Arvo",serif}
.b1 .t2{position:absolute;left:88px;top:40px;font:400 30px "Open Sans",sans-serif;color:#fff}
.b2 .t1{position:absolute;left:78px;top:22px;font:700 16px "Arvo",serif}
.b2 .t2{position:absolute;left:76px;top:44px;font:400 26px "Arvo",serif;color:#fff}
.b3 .t1{position:absolute;left:74px;top:24px;font:700 12.5px "Arvo",serif;line-height:16px;color:#1a1a1a}
.b3 .t1 em{font-style:normal;color:#fff}

.products{left:109px;top:485px;width:553px;height:213px;background:var(--white);border-radius:4px}
.card{top:19px;width:144px;height:175px;border:1px solid var(--card-line);background:#fff}
.card .pic{margin:8px 0 0 6px;width:130px;height:130px}
.card .cap{position:absolute;left:0;right:0;bottom:4px;height:29px;background:#ebebeb;font:400 7.5px "Oswald",sans-serif;color:#111;text-align:center;line-height:29px}
.round{width:32px;height:32px;border-radius:50%;background:linear-gradient(#fff,#ddd);border:1px solid #222;display:flex;align-items:center;justify-content:center}

.footer{left:0;top:716px;width:770px;height:207px;background:var(--footer)}
.footer-base{left:0;top:923px;width:770px;height:33px;background:var(--footer-base);font-size:6px;color:#777;padding:14px 0 0 91px}
.col h4{font:400 9px "Oswald",sans-serif;color:#fff;margin-bottom:10px}
.col ul{list-style:none;width:108px}
.col li{font-size:6px;color:#8a8a8a;border-bottom:1px solid var(--line);padding:0 0 5px;margin-bottom:5px}
.about p{width:293px;font-size:6px;line-height:11px;color:#888}
.signup{font-size:6px;color:#888;margin:-4px 0 9px}
.news{display:flex;gap:4px}
.news .field{width:177px;height:21px;background:#fff;border-radius:3px}
.news .sub{width:62px;height:21px;border-radius:3px;background:linear-gradient(#d4b293,#9c7657);font:400 9px "Oswald",sans-serif;text-align:center;line-height:21px}
.pay{margin-top:18px;width:186px;height:22px;background:#1b1b1b;border-radius:3px;display:flex;align-items:center;gap:3px;padding-left:5px;font-size:5.5px;color:#888}
.pay .card-name{background:#fff;color:#222;font-size:4.6px;font-weight:600;height:12px;padding:0 2px;line-height:12px;border-radius:1px;min-width:20px;text-align:center}
.pay .card-name:first-of-type{margin-left:6px}
</style>
</head>
<body>
<div class="page">
  <div class="abs welcome">Welcome to our online store!</div>
  <div class="abs top-links"><span>MY ACCOUNT</span><span class="sep">|</span><span>MY WISHLIST</span><span class="sep">|</span><span>MY CART</span><span class="sep">|</span><span>CHECKOUT</span><span class="sep">|</span><span>LOG IN</span></div>
  <div class="abs cart">
    <svg width="18" height="13" viewBox="0 0 18 13"><path d="M1 1h3l2 8h9l2-6H5" fill="none" stroke="#b08b6a" stroke-width="1.4"/><circle cx="7" cy="11.5" r="1.2" fill="#b08b6a"/><circle cx="14" cy="11.5" r="1.2" fill="#b08b6a"/></svg>
    Shopping Cart 0 item added
  </div>
  <div class="abs logo">Jewelry</div>
  <div class="abs search"><div class="field">Search entire store here...</div><div class="btn"><svg width="11" height="11" viewBox="0 0 11 11"><circle cx="4.5" cy="4.5" r="3.3" fill="none" stroke="#fff" stroke-width="1.4"/><path d="M7 7l3 3" stroke="#fff" stroke-width="1.6"/></svg></div></div>
  <nav class="abs nav"><a href="#">NEW PRODUCTS</a><a href="#" class="active">SPECIALS</a><a href="#">FURNITURE</a><a href="#">ELECTRONICS</a><a href="#">APPAREL</a><a href="#">ALL PRODCUTS</a></nav>

  <div class="abs hero-glow"></div>
  <div class="abs hero-img" role="img" aria-label="Gold ring set with rows of clear stones"></div>
  <div class="abs arrow" style="left:91px;top:228px"><svg width="12" height="18" viewBox="0 0 12 18"><path d="M9 2L3 9l6 7" fill="none" stroke="#fff" stroke-width="3"/></svg></div>
  <div class="abs arrow" style="left:640px;top:228px"><svg width="12" height="18" viewBox="0 0 12 18"><path d="M3 2l6 7-6 7" fill="none" stroke="#fff" stroke-width="3"/></svg></div>
  <div class="abs hero-title">HEROES OF WAR</div>
  <div class="abs hero-sub">SALE 25% OFF + FREE SHIPPING</div>
  <div class="abs shop"><div class="ico"><svg width="18" height="13" viewBox="0 0 18 13"><path d="M1 1h3l2 8h9l2-6H5" fill="none" stroke="#ccc" stroke-width="1.4"/><circle cx="7" cy="11.5" r="1.2" fill="#ccc"/><circle cx="14" cy="11.5" r="1.2" fill="#ccc"/></svg></div><span>SHOP NOW !</span></div>
  <div class="abs dots"><i></i><i></i><i></i></div>

  <section class="abs promo">
    <div class="banner b1"><div class="pic" role="img" aria-label="Silver pendant necklace with coloured stones"></div><div class="t1">SAVE UP TO</div><div class="t2">25%</div></div>
    <div class="banner b2"><div class="pic" role="img" aria-label="Silver flower ring with red stones"></div><div class="t1">SPECIAL</div><div class="t2">OFFERS</div></div>
    <div class="banner b3"><div class="pic" role="img" aria-label="Pair of silver drop earrings with red stones"></div><div class="t1">FREE SHIPPING<br><em>on Purchases<br>Over $99</em></div></div>
  </section>

  <section class="abs products">
    <div class="abs card" style="left:29px"><div class="pic" role="img" aria-label="Pearl necklace with silver clasp" style="background:radial-gradient(circle at 50% 50%,#f4f4f4,#c9c9c9 70%,#555)"></div><div class="cap">LOREMIPSUM QUIA DOLOR SIT AMET</div></div>
    <div class="abs card" style="left:204px"><div class="pic" role="img" aria-label="Engraved silver cuff bracelet" style="background:radial-gradient(circle,#8f8f8f,#fff 75%)"></div><div class="cap">LOREMIPSUM QUIA DOLOR SIT AMET</div></div>
    <div class="abs card" style="left:378px"><div class="pic" role="img" aria-label="Pair of silver wedding rings" style="background:radial-gradient(circle,#bdbdbd,#f3f1ef 70%)"></div><div class="cap">LOREMIPSUM QUIA DOLOR SIT AMET</div></div>
  </section>
  <div class="abs round" style="left:90px;top:570px"><svg width="8" height="12" viewBox="0 0 8 12"><path d="M6 1L2 6l4 5" fill="none" stroke="#9c7657" stroke-width="2.2"/></svg></div>
  <div class="abs round" style="left:649px;top:570px"><svg width="8" height="12" viewBox="0 0 8 12"><path d="M2 1l4 5-4 5" fill="none" stroke="#9c7657" stroke-width="2.2"/></svg></div>

  <footer class="abs footer">
    <div class="abs col" style="left:91px;top:13px"><h4>INFORMATION</h4><ul><li>About Us</li><li>Customer Service</li><li>Contact Us</li></ul></div>
    <div class="abs col" style="left:91px;top:92px"><h4>CONNECT WITH US</h4><ul><li>Chatter</li><li>Friendwall</li><li>Blog</li><li>Vidstream</li></ul></div>
    <div class="abs col" style="left:238px;top:13px"><h4>SERVICES &amp; SUPPORT</h4><ul><li>Customer Assistance</li><li>FAQs</li><li>International Shipping</li><li>Returns</li><li>Policies</li></ul></div>
    <div class="abs col about" style="left:384px;top:13px">
      <h4>ABOUT THE STORE</h4>
      <p>Lorem Ipsum is simply dummy text of the printing and typesetting industry. Lorem Ipsum has been the industry's standard dummy text ever since the 1500s, when an unknown printer took a galley of type and scrambled it to make a type specimen book. It has survived not only five centuries, but also the leap into electronic typesetting, remaining essentially unchanged.</p>
      <h4 style="margin-top:14px">NEWSLETTER</h4>
      <div class="signup">Sign Up for Our Newsletter</div>
      <div class="news"><div class="field"></div><div class="sub">SUBSCRIBE</div></div>
      <div class="pay">Payment Method<span class="card-name">Corvia</span><span class="card-name">Amexa</span><span class="card-name">Nexa</span><span class="card-name">Orbis</span><span class="card-name">Tendrix</span></div>
    </div>
  </footer>
  <div class="abs footer-base">© 2007 Lumen Demo Store. All Rights Reserved.</div>
</div>
</body>
</html>
```